Seasonal Postcard - Branding Campaign for Mechanical Company

Postcard branding campaign. Image size must be 2775x1875 pixels landscape only. JPEG or PNG format. Cannot exceed 10MB. Looking for multiple designs for different monthly postcards to send to existing customer 2x a month. Go to www.brightforgeservicesnc.com for color schemes and design feel. Seasonal postcard for Spring, Summer, Fall and Winter Feel for promoting our residential plumbing, electrical, heating and cooling(HVAC) and generator repair and maintenance services. Clean, non cluttered design. You can design to include all services, or just target one service and one season. Some coupons can be offered for each department (HVAC - $49 Off HVAC Check Up) (Generator - $300 Off Generator Installation) (Electrical - Free Electrical Panel Inspection) (Plumbing - $50 Off Water Heater Installation)

Target Market(s)

Homeowners age 35+

Colors

Designer to choose colors to be used in the design.

Requirements
Should not have
• any phone numbers (please photoshop off of any images of vehicles)

```html
<!DOCTYPE html>
<html lang="en">
<head>
<meta charset="utf-8">
<title>Brightforge Services – Winter Postcard</title>
<link href="https://fonts.googleapis.com/css2?family=Oswald:wght@500;600&family=Lato:wght@400;700;900&display=swap" rel="stylesheet">
<style>
  :root{
    --navy:#1f2d6b;
    --navy-deep:#18245a;
    --red:#e21f26;
    --red-dark:#c8161d;
    --white:#ffffff;
    --ink:#1b1b1b;
    --stage:#a3a3a3;
    --snow:#e9eef6;
    --line:#9a9a9a;
  }
  *{margin:0;padding:0;box-sizing:border-box}
  html,body{width:902px;height:1200px;overflow:hidden;background:var(--stage)}
  .stage{width:930px;height:1237px;position:relative;transform:scale(0.9699);transform-origin:0 0;font-family:'Lato',sans-serif}
  .side-label{position:absolute;font:700 27px 'Lato',sans-serif;color:#222}
  .side-label.front{left:711px;top:24px}
  .side-label.back{left:737px;top:1152px}

  .card{position:absolute;width:708px;height:478px;background:var(--white);overflow:hidden}
  .card.front{left:93px;top:80px}
  .card.back{left:123px;top:640px}

  .abs{position:absolute}
  .scene-photo{left:200px;top:90px;width:360px;height:250px;background:linear-gradient(135deg,#d9dde6,#eef0f4 60%,#f6f6f8);opacity:.9}
  .swoosh{left:0;top:0;width:708px;height:478px}
  .products{left:340px;top:110px;width:365px;height:250px;background:radial-gradient(ellipse at 55% 50%,#d7d9db 0%,#bfc3c6 45%,rgba(190,195,200,0) 75%)}

  .headline{left:28px;top:20px;font:500 55px/1 'Oswald',sans-serif;color:var(--navy);letter-spacing:-1px;white-space:nowrap}
  .subhead{left:30px;top:84px;font:500 32px/1 'Oswald',sans-serif;color:var(--red);letter-spacing:-.5px;white-space:nowrap}
  .services-title{left:30px;top:139px;font:500 22px/1 'Oswald',sans-serif;color:var(--navy)}
  .services-title span{color:var(--red)}
  .service-list{left:30px;top:175px;list-style:none}
  .service-list li{display:flex;align-items:center;height:27.7px;font:700 16px 'Lato',sans-serif;color:var(--navy)}
  .service-list .dot{width:20px;height:20px;border-radius:50%;background:var(--red);margin-right:12px}

  .brand{display:flex;align-items:center;gap:8px}
  .brand-name{font:900 30px/0.95 'Lato',sans-serif;color:var(--navy);letter-spacing:.5px;white-space:nowrap}
  .brand-name small{display:block;font-size:17px;letter-spacing:4.6px}
  .brand-mark{width:40px;height:40px;background:var(--red)}
  .front .brand{left:397px;top:28px}
  .back .brand{left:78px;top:28px}

  .badges{left:26px;top:298px;width:300px}
  .badge{position:absolute;background:#d5d8e0;border-radius:4px}

  .visit{font:700 13px 'Lato',sans-serif;letter-spacing:.3px;white-space:nowrap}
  .front .visit{left:343px;top:393px;color:var(--white)}
  .url-pill{background:var(--red);color:var(--white);border-radius:17px;font:700 20px/34px 'Lato',sans-serif;text-align:center;white-space:nowrap}
  .front .url-pill{left:295px;top:418px;width:385px;height:34px;font-size:19.5px}

  .coupon-panel{left:0;top:92px;width:418px;height:270px;background:linear-gradient(180deg,var(--red),var(--red-dark))}
  .coupon{position:absolute;width:145px;height:112px;background:var(--white);border:2px dashed var(--red);outline:2px solid var(--white);white-space:nowrap}
  .coupon .tag{height:30px;background:var(--navy);color:var(--white);font:400 18px/30px 'Lato',sans-serif;padding-left:8px}
  .coupon .price{font:600 34px/1 'Oswald',sans-serif;color:var(--red);padding:8px 0 2px 7px;letter-spacing:-.5px}
  .coupon .note{font:700 13px 'Lato',sans-serif;color:var(--ink);padding-left:9px}
  .coupon .note.sm{font-size:8.5px;padding-top:3px}
  .coupon .icon{position:absolute;right:-14px;top:-16px;width:36px;height:36px;border-radius:50%;background:var(--white);border:2px solid var(--ink);display:flex;align-items:center;justify-content:center}
  .free-line{display:flex;align-items:flex-end;gap:3px}
  .free-line em{font:700 8.5px 'Lato',sans-serif;font-style:normal;color:var(--ink);padding-bottom:4px}

  .snow-band{left:0;top:362px;width:418px;height:116px;background:linear-gradient(180deg,#f3f6fb,var(--snow))}
  .back .visit{left:67px;top:382px;color:var(--ink)}
  .back .url-pill{left:20px;top:405px;width:382px;height:34px}

  .stamp{left:582px;top:36px;width:92px;height:90px;border:1px solid #bbb}
  .address-line{left:443px;width:238px;height:1px;background:var(--line)}
</style>
</head>
<body>
<div class="stage">
  <div class="side-label front">Front</div>

  <section class="card front">
    <div class="abs scene-photo" role="img" aria-label="Faint winter photo of children in snow beside a service van"></div>
    <svg class="abs swoosh" viewBox="0 0 708 478" aria-hidden="true">
      <path d="M600 100 C650 110 690 115 708 105 L708 165 C680 160 640 140 600 130 Z" fill="var(--red)"/>
      <path d="M0 355 C120 420 260 410 420 320 C520 262 620 230 708 232 L708 478 L0 478 Z" fill="var(--red)"/>
      <path d="M0 372 C120 430 270 425 425 335 C525 278 620 248 708 250 L708 478 L0 478 Z" fill="var(--white)"/>
      <path d="M0 384 C130 440 280 432 430 346 C530 290 625 262 708 265 L708 478 L0 478 Z" fill="var(--navy)"/>
    </svg>
    <div class="abs products" role="img" aria-label="Air handler, outdoor AC unit, standby generator and smart thermostat"></div>

    <h1 class="abs headline">YOUR FRIENDLY</h1>
    <h2 class="abs subhead">FULL-SERVICE COMPANY!</h2>
    <h3 class="abs services-title">OUR <span>SERVICES</span></h3>
    <ul class="abs service-list">
      <li><span class="dot"></span>Residential plumbing</li>
      <li><span class="dot"></span>Electrical</li>
      <li><span class="dot"></span>Heating and cooling(HVAC)</li>
      <li><span class="dot"></span>Generator repair and maintenance</li>
    </ul>

    <div class="abs brand">
      <div class="brand-name">BRIGHTFORGE<small>SERVICES</small></div>
      <div class="brand-mark"></div>
    </div>

    <div class="abs badges" aria-label="Partner and certification badges">
      <div class="badge" style="left:0;top:0;width:60px;height:18px"></div>
      <div class="badge" style="left:68px;top:0;width:62px;height:18px"></div>
      <div class="badge" style="left:138px;top:0;width:92px;height:18px"></div>
      <div class="badge" style="left:238px;top:0;width:24px;height:22px"></div>
      <div class="badge" style="left:280px;top:4px;width:20px;height:16px"></div>
      <div class="badge" style="left:0;top:28px;width:100px;height:14px"></div>
      <div class="badge" style="left:112px;top:34px;width:50px;height:22px"></div>
      <div class="badge" style="left:180px;top:32px;width:34px;height:34px;border-radius:50%"></div>
      <div class="badge" style="left:228px;top:26px;width:36px;height:44px"></div>
      <div class="badge" style="left:30px;top:52px;width:60px;height:14px"></div>
      <div class="badge" style="left:118px;top:66px;width:26px;height:34px"></div>
      <div class="badge" style="left:174px;top:76px;width:36px;height:34px"></div>
    </div>

    <p class="abs visit">VISIT US TODAY FOR MORE INFORMATION :</p>
    <div class="abs url-pill">www.brightforgeservicesnc.com</div>
  </section>

  <section class="card back">
    <div class="abs brand">
      <div class="brand-name">BRIGHTFORGE<small>SERVICES</small></div>
      <div class="brand-mark"></div>
    </div>

    <div class="abs coupon-panel"></div>

    <div class="coupon" style="left:28px;top:112px">
      <div class="tag">HVAC</div>
      <div class="price">$49 OFF</div>
      <div class="note">HVAC CHECK UP</div>
      <div class="icon"><svg width="20" height="20" viewBox="0 0 20 20"><circle cx="6" cy="5" r="3" fill="var(--ink)"/><path d="M2 18v-6l4-3 4 3v6z" fill="var(--ink)"/><rect x="11" y="9" width="8" height="9" fill="none" stroke="var(--ink)" stroke-width="1.6"/></svg></div>
    </div>
    <div class="coupon" style="left:223px;top:112px">
      <div class="tag">GENERATOR</div>
      <div class="price">$300 OFF</div>
      <div class="note sm">GENERATOR INSTALLATION</div>
      <div class="icon"><svg width="20" height="20" viewBox="0 0 20 20"><rect x="2" y="5" width="16" height="12" fill="none" stroke="var(--ink)" stroke-width="1.6"/><rect x="4" y="3" width="3" height="2" fill="var(--ink)"/><rect x="13" y="3" width="3" height="2" fill="var(--ink)"/><path d="M11 7l-3 5h3l-2 4 4-6h-3z" fill="var(--ink)"/></svg></div>
    </div>
    <div class="coupon" style="left:28px;top:236px">
      <div class="tag">ELECTRICAL</div>
      <div class="free-line"><div class="price">FREE</div><em>ELECTRICAL</em></div>
      <div class="note">PANEL INSPECTION</div>
      <div class="icon" style="background:var(--ink)"><svg width="20" height="20" viewBox="0 0 20 20"><path d="M12 1L4 11h5l-2 8 9-11h-5z" fill="var(--white)"/></svg></div>
    </div>
    <div class="coupon" style="left:223px;top:236px">
      <div class="tag">PLUMBING</div>
      <div class="price">$50 OFF</div>
      <div class="note sm">WATER HEATER INSTALLATION</div>
      <div class="icon"><svg width="20" height="20" viewBox="0 0 20 20"><path d="M2 9l8-7 8 7v9H2z" fill="none" stroke="var(--ink)" stroke-width="1.6"/><path d="M10 8c-2 3-3 4-3 6a3 3 0 006 0c0-2-1-3-3-6z" fill="var(--ink)"/></svg></div>
    </div>

    <div class="abs snow-band"></div>
    <p class="abs visit">VISIT US TODAY FOR MORE INFORMATION :</p>
    <div class="abs url-pill">www.brightforgeservicesnc.com</div>

    <div class="abs stamp"></div>
    <div class="abs address-line" style="top:250px"></div>
    <div class="abs address-line" style="top:294px"></div>
    <div class="abs address-line" style="top:348px"></div>
  </section>

  <div class="side-label back">Back</div>
</div>
</body>
</html>
```